New Business Card Design Project for Handyman Business

I would like to purchase a customized version of a design you have previously submitted - https://www.artvelloshowcase.com/design/58172046
I love this design!
I am hoping you can design something similar to this for our Handyman Business.
Attached is our logo and some graphics we have used.
Here is a link to the Google Doc with the content that needs to be included, https://files.quorvandel.net/document/d/e/4QZTR-8kPw2LmXn5Hb7rYcVt-qaaJsK3Df9TgNpU4WeR__LmcXaBvKpHsd2Qjn7wo4tzhgrVb41K85o3ttSTq/pub
Target Market(s)
Real Estate Agents, Home Owners and Property Managers
Industry/Entity Type
Construction/ Speciality Trade
Contact Information for Business Card
https://files.quorvandel.net/document/d/7QwRtYpL_zxkn4BvHnCdFs8TmKjWaEr2LUXPo6cxhg/edit?usp=sharing
Font styles to use
Other font styles liked:
- Ubuntu
Look and feel
Each slider illustrates characteristics of the customer's brand and the style your logo design should communicate.

```html
<!DOCTYPE html>
<html lang="en">
<head>
<meta charset="utf-8">
<title>brightfix – Business Card</title>
<link rel="stylesheet" href="https://fonts.googleapis.com/css2?family=Ubuntu:wght@400;500;700&display=swap">
<style>
  :root {
    --stage: #232323;
    --brand-blue: #1a7bc4;
    --brand-blue-deep: #136aae;
    --brand-green: #45b649;
    --brand-orange: #ef7a3a;
    --card-dark: #1f1f21;
    --card-dark-2: #262628;
    --card-dark-3: #2c2c2f;
    --text-light: #ffffff;
  }
  * { box-sizing: border-box; margin: 0; padding: 0; }
  html, body { width: 1200px; height: 780px; overflow: hidden; }
  body {
    background: var(--stage);
    font-family: "Ubuntu", sans-serif;
    position: relative;
  }
  .card {
    position: absolute;
    top: 110px;
    width: 320px;
    height: 560px;
    border-radius: 22px;
    overflow: hidden;
    box-shadow: 0 18px 40px rgba(0,0,0,.55);
  }

  /* Front */
  .card--front { left: 230px; background: var(--brand-blue); }
  .front-pattern {
    position: absolute; inset: 0;
    background: linear-gradient(160deg, #3a8fd0 0%, var(--brand-blue) 45%, var(--brand-blue-deep) 100%);
  }
  .front-brand {
    position: absolute;
    left: 50%; top: 50%;
    transform: translate(-50%, -50%) rotate(-90deg);
    display: flex; align-items: center; gap: 18px;
    white-space: nowrap;
  }
  .front-brand__mark { width: 58px; height: 58px; background: var(--text-light); }
  .front-brand__text { display: flex; flex-direction: column; color: var(--text-light); }
  .front-brand__name { font-size: 66px; font-weight: 500; line-height: 1; letter-spacing: -1px; }
  .front-brand__tagline { font-size: 13px; font-weight: 500; letter-spacing: 3px; margin-top: 4px; }

  /* Back */
  .card--back { left: 650px; background: var(--card-dark); }
  .back-layers { position: absolute; inset: 0; }
  .back-content {
    position: relative;
    display: flex; flex-direction: column; align-items: center;
    text-align: center;
    padding-top: 48px;
    color: var(--text-light);
  }
  .logo { display: flex; align-items: center; gap: 10px; }
  .logo__mark { width: 30px; height: 30px; background: var(--brand-green); }
  .logo__name { font-size: 44px; font-weight: 500; color: var(--brand-blue); line-height: 1; letter-spacing: -0.5px; }
  .logo__tagline { font-size: 11px; font-weight: 500; color: var(--brand-orange); letter-spacing: 2.6px; margin-top: 6px; }

  .person { margin-top: 38px; }
  .person__name { font-size: 30px; font-weight: 700; line-height: 1; }
  .person__first { color: var(--brand-blue); }
  .person__last { color: var(--brand-green); }
  .person__role { font-size: 15px; font-weight: 500; margin-top: 6px; }

  .contact-icons { display: flex; gap: 8px; margin-top: 14px; }
  .icon-dot {
    width: 24px; height: 24px; border-radius: 50%;
    background: var(--brand-green);
    display: flex; align-items: center; justify-content: center;
  }
  .icon-dot svg { width: 13px; height: 13px; }
  .contact-list { list-style: none; margin-top: 12px; font-size: 14px; line-height: 1.5; }

  .social-dots { display: flex; gap: 9px; margin-top: 16px; }
  .social-dots .icon-dot { width: 22px; height: 22px; }
  .social-handle { font-size: 13.5px; margin-top: 10px; }

  .services {
    position: absolute; left: 0; right: 0; bottom: 34px;
    text-align: center; color: var(--text-light);
    font-size: 13.5px; line-height: 1.5;
  }
  .services__list { display: flex; justify-content: center; align-items: center; gap: 6px; }
  .bullet { width: 9px; height: 9px; border-radius: 50%; background: var(--brand-green); display: inline-block; }
</style>
</head>
<body>

<section class="card card--front" aria-label="Card front">
  <div class="front-pattern" role="img" aria-label="Repeating pattern of the company symbol in tonal blue"></div>
  <div class="front-brand">
    <span class="front-brand__mark"></span>
    <div class="front-brand__text">
      <span class="front-brand__name">brightfix</span>
      <span class="front-brand__tagline">HOME CARE SPECIALISTS</span>
    </div>
  </div>
</section>

<section class="card card--back" aria-label="Card back">
  <svg class="back-layers" viewBox="0 0 320 560" preserveAspectRatio="none" aria-hidden="true">
    <rect width="320" height="560" fill="var(--card-dark-2)"/>
    <path d="M0 560 V470 Q160 380 320 430 V560 Z" fill="var(--card-dark)"/>
    <path d="M0 0 H320 V400 Q170 470 0 420 Z" fill="var(--card-dark-3)"/>
    <path d="M0 0 H320 V380 Q170 450 0 400 Z" fill="var(--card-dark)"/>
  </svg>

  <div class="back-content">
    <div class="logo">
      <span class="logo__mark"></span>
      <span class="logo__name">brightfix</span>
    </div>
    <p class="logo__tagline">HOME CARE SPECIALISTS</p>

    <div class="person">
      <h1 class="person__name"><span class="person__first">Dana</span> <span class="person__last">Whitlow</span></h1>
      <p class="person__role">Owner/ Handyman</p>
    </div>

    <div class="contact-icons">
      <span class="icon-dot" aria-label="Phone">
        <svg viewBox="0 0 16 16"><path d="M4 1.5 6.2 4 5 5.6q1.5 3.2 5.4 5.4L12 9.8l2.5 2.2-1.6 2.4Q6 13.5 1.6 3.1Z" fill="#fff"/></svg>
      </span>
      <span class="icon-dot" aria-label="Email">
        <svg viewBox="0 0 16 16"><rect x="1.5" y="3.5" width="13" height="9" fill="none" stroke="#fff" stroke-width="1.6"/><path d="M2 4l6 5 6-5" fill="none" stroke="#fff" stroke-width="1.6"/></svg>
      </span>
      <span class="icon-dot" aria-label="Website">
        <svg viewBox="0 0 16 16"><circle cx="8" cy="8" r="6.3" fill="none" stroke="#fff" stroke-width="1.4"/><ellipse cx="8" cy="8" rx="2.8" ry="6.3" fill="none" stroke="#fff" stroke-width="1.2"/><path d="M1.8 8h12.4" stroke="#fff" stroke-width="1.2"/></svg>
      </span>
    </div>

    <ul class="contact-list">
      <li>(555) 214-7730</li>
      <li>www.brightfix-homes.com</li>
      <li>dana@brightfix-homes.com</li>
    </ul>

    <div class="social-dots" aria-label="Social profiles">
      <span class="icon-dot"></span>
      <span class="icon-dot"></span>
      <span class="icon-dot"></span>
      <span class="icon-dot"></span>
    </div>
    <p class="social-handle">BrightfixHandymanServices</p>
  </div>

  <div class="services">
    <p>Commercial and Resdiential Handyman</p>
    <p class="services__list">Improve <span class="bullet"></span> Repair <span class="bullet"></span> Remodel <span class="bullet"></span> Maintain</p>
  </div>
</section>

</body>
</html>
```